Bright Meadow Counseling Business Card design with a visually interesting use of Space

I need business cards that are luxurious and give a peaceful, calm vibe. I also had some letterhead designed, and i like the look of it also, it's attached with the logo design for reference/ ideas but feel free to be creative.

Target Market(s)

High end luxurious client who needs counseling

Industry/Entity Type

Marriage and Family Therapy

Contact Information for Business Card

Mira Kowalczyk MS LMFT/ or Toby Hallett address 4150 Larkin Suite 600

Font styles to use
Sans Serif

Colors
0054AA
0677BA
7BADD7
CADEEF
E8F1F8
0094D4
00A9DD
6FCCEA
C7EBF8
E9F6FB
A7469A
B969AE
D3A5CF
EDDBEB
F8F0F9
6B429C
8869AF
B7A5CE
E3DAEB
F3F0F8

Requirements
Must have
• Logo and color scheme but be simple modern and luxurious
Nice to have
• I'd like to incorporate some elelmets from the logo and letterhead into a simple modern card

```html
<!DOCTYPE html>
<html lang="en">
<head>
<meta charset="utf-8">
<title>Bright Meadow Counseling – Business Card</title>
<link href="https://fonts.googleapis.com/css2?family=Poppins:wght@300&display=swap" rel="stylesheet">
<style>
  :root {
    --backdrop: #2e2e2e;
    --card: #ffffff;
    --ink: #1a1a1a;
    --plum: #a7469a;
    --violet: #8869af;
    --orchid: #b969ae;
    --teal: #5dbcb9;
  }
  * { margin: 0; padding: 0; box-sizing: border-box; }
  html, body {
    width: 1200px;
    height: 1200px;
    overflow: hidden;
    background: var(--backdrop);
    font-family: "Poppins", sans-serif;
    font-weight: 300;
    color: var(--ink);
  }
  .card {
    position: absolute;
    left: 239px;
    width: 722px;
    height: 412px;
    background: var(--card);
    border-radius: 22px;
  }
  .card--front { top: 140px; }
  .card--back { top: 645px; }

  .brand-mark {
    position: absolute;
    display: flex;
    align-items: center;
    gap: 10px;
    font-weight: 300;
    white-space: nowrap;
  }
  .brand-mark__dot {
    border-radius: 50%;
    background: var(--violet);
    flex: none;
  }

  .card--front .brand-mark {
    top: 82px;
    right: 38px;
    font-size: 17px;
    line-height: 1.3;
    color: var(--violet);
    text-align: right;
  }
  .card--front .brand-mark__dot { width: 14px; height: 14px; }

  .holder {
    position: absolute;
    left: 38px;
    top: 168px;
  }
  .holder__name {
    font-size: 37px;
    font-weight: 300;
    letter-spacing: 1.5px;
    line-height: 1;
    text-transform: uppercase;
  }
  .holder__credentials {
    margin-top: 8px;
    font-size: 21px;
    font-weight: 300;
    color: var(--orchid);
    line-height: 1;
  }

  .contact {
    position: absolute;
    left: 38px;
    top: 248px;
    list-style: none;
  }
  .contact__item {
    display: flex;
    align-items: center;
    height: 31px;
    font-size: 20px;
    letter-spacing: 0.5px;
  }
  .contact__icon {
    width: 18px;
    height: 18px;
    margin-right: 12px;
    fill: var(--plum);
    flex: none;
  }

  .stripe {
    position: absolute;
    left: 40px;
    right: 38px;
    bottom: 40px;
    display: flex;
    gap: 4px;
    height: 5px;
  }
  .stripe span { flex: 1; }
  .stripe .violet { background: var(--violet); }
  .stripe .plum { background: var(--plum); }
  .stripe .teal { background: var(--teal); }

  .card--back .brand-mark {
    top: 160px;
    left: 0;
    right: 0;
    justify-content: center;
    gap: 14px;
    color: var(--ink);
    font-size: 34px;
    line-height: 1.2;
  }
  .card--back .brand-mark__dot { width: 22px; height: 22px; }
</style>
</head>
<body>
  <section class="card card--front">
    <div class="brand-mark">
      <span>Bright Meadow<br>Counseling</span>
      <span class="brand-mark__dot"></span>
    </div>

    <div class="holder">
      <h1 class="holder__name">Mira Kowalczyk</h1>
      <p class="holder__credentials">MS LMFT</p>
    </div>

    <ul class="contact">
      <li class="contact__item">
        <svg class="contact__icon" viewBox="0 0 24 24" aria-hidden="true"><path d="M6.6 10.8a15.1 15.1 0 0 0 6.6 6.6l2.2-2.2a1 1 0 0 1 1-.25 11.4 11.4 0 0 0 3.6.57 1 1 0 0 1 1 1V20a1 1 0 0 1-1 1A17 17 0 0 1 3 4a1 1 0 0 1 1-1h3.5a1 1 0 0 1 1 1c0 1.25.2 2.45.57 3.6a1 1 0 0 1-.25 1z"/></svg>
        555-204-7318
      </li>
      <li class="contact__item">
        <svg class="contact__icon" viewBox="0 0 24 24" aria-hidden="true"><path d="M2 5h20v14H2z"/><path d="M2 5l10 7 10-7v2l-10 7L2 7z" fill="#fff"/></svg>
        hello@brightmeadow.com
      </li>
      <li class="contact__item">
        <svg class="contact__icon" viewBox="0 0 24 24" aria-hidden="true"><path d="M12 2a7 7 0 0 0-7 7c0 5.2 7 13 7 13s7-7.8 7-13a7 7 0 0 0-7-7zm0 9.5A2.5 2.5 0 1 1 12 6.5a2.5 2.5 0 0 1 0 5z"/></svg>
        4150 Larkin Suite 600
      </li>
    </ul>

    <div class="stripe"><span class="violet"></span><span class="plum"></span><span class="plum"></span><span class="teal"></span></div>
  </section>

  <section class="card card--back">
    <div class="brand-mark">
      <span>Bright Meadow Counseling</span>
      <span class="brand-mark__dot"></span>
    </div>
    <div class="stripe"><span class="violet"></span><span class="plum"></span><span class="plum"></span><span class="teal"></span></div>
  </section>
</body>
</html>
```